Cool Landing page with email address sign up (mockups provided)

I need a landing page for a service that will send a weekly email to people who are looking for jobs in startups. On the landing page there is a call to action (submit button) to register their email address. The service is called VentureRoster and it is a side project to try to assist startup companies with hiring people.

I just want one single form field "Email".

The feeling I want to give people is one of adventure. Imagine the person is living in Gdansk Poland, they are a technical/IT expert and have dreams of making it big in a Startup in London. This is his big chance, this is going to allow him to do it! He's signing up to a big promise! It should be cool, professional, exciting.

A major influence should be:
http://copperkettlefair.example/

There should also be a call to tweet in a cool way like on (http://www.behindfounders.example/).

Look at this - taking a leap of faith, like this:
http://pagebloomkit.example/wp-content/uploads/2011/09/19.jpg

This is super with the colours - striking!:
http://hueparlor.example/

Fly your kit higher!:
http://tobiasvrenn.example/

If necessary use sex to sell:
http://pagebloomkit.example/wp-content/uploads/2011/09/24.jpg

Some original art would work:
http://pagebloomkit.example/wp-content/uploads/2011/09/fx_ss_group1_sm_filtered_0000s_0007_Layer-14.jpg

This is effective for a call to action, I'm looking to you to act!:
http://pagebloomkit.example/wp-content/uploads/2011/09/weblance.jpg
Take inspiration from:
http://www.behindfounders.example/
http://ventureroster.example/
http://foundersdaily.example/

***N.B.: I would prefer original art background over a photo

Also:
http://pixeljournalhub.example/inspiration/a-showcase-of-landing-pages-designed-for-conversion
especially:
http://pixeljournalhub.example/wp-content/uploads/2011/09/01-landing.jpg
http://pixeljournalhub.example/wp-content/uploads/2011/09/04-landing.jpg
http://pixeljournalhub.example/wp-content/uploads/2011/10/texture21.jpg

I really like the colouring from Coder Bulletin:
http://news.quillforge.example/

Reason: I'm going to be away for a few days so I won't have enough time to properly provide feedback.

The payment is now guaranteed. This project is a single page only.

I've added a few more example landing pages that I like.

I've now added the ventureroster logo image that should be used.

I've updated brief with more examples of what I'm looking for

Reason: I'm still progressing with candidate designs.

Target Market(s)

Technical people, english not being their native language. Ambitious to work in London/Dublin in a tech startup company. They want to receive a weekly emails with startup jobs in london or dublin.

Requirements
Must have
• Eyes must be drawn to the email registration form to get them to submit their email address. The background image or website theme should encourage their desires to work in the big city in exciting startup companies.

Should have a prompt to tweet (once pressed I'll do my own popup)

```html
<!DOCTYPE html>
<html lang="en">
<head>
<meta charset="utf-8">
<title>VentureRoster — Weekly startup jobs</title>
<link rel="stylesheet" href="https://fonts.googleapis.com/css2?family=Gelasio:wght@700&family=Arimo:ital,wght@0,700;1,400&family=Handlee&display=swap">
<style>
  :root {
    --sky: #d4dafc;
    --night: #2a2b2f;
    --gold: #b08c10;
    --cream: #fdf1d0;
    --ink: #2e2e30;
    --skyline-top: #1a1a1c;
    --skyline-bottom: #050506;
    --globe-top: #2c5fd6;
    --globe-bottom: #0a2886;
    --field-top: #f4f4f4;
    --field-bottom: #d2d2d2;
    --placeholder: #8a8a8a;
    --button-top: #2456d8;
    --button-bottom: #0c2f9a;
    --chirp-dot: #8fd3f0;
    --chirp-text: #1f7f9a;
  }
  * { box-sizing: border-box; margin: 0; padding: 0; }
  html, body { width: 1200px; height: 1200px; overflow: hidden; }
  body {
    position: relative;
    background: var(--sky);
    font-family: "Arimo", Arial, sans-serif;
  }
  .night-disc {
    position: absolute;
    left: 514px; top: -376px;
    width: 1330px; height: 1345px;
    border-radius: 50%;
    background: var(--night);
    box-shadow: 0 0 14px 6px rgba(42, 43, 47, 0.55);
  }
  .brand {
    position: absolute;
    left: 35px; top: 72px;
    font-family: "Gelasio", Georgia, serif;
    font-weight: 700;
    font-size: 55px;
    line-height: 70px;
    color: var(--gold);
    letter-spacing: -0.5px;
  }
  .pitch {
    position: absolute;
    left: 581px; top: 166px;
    width: 600px;
    font-weight: 700;
    font-size: 30.5px;
    line-height: 40px;
    color: var(--cream);
  }
  .signup-form { position: absolute; left: 0; top: 0; }
  .email-field {
    position: absolute;
    left: 667px; top: 594px;
    width: 487px; height: 82px;
    border: 1px solid #bdbdbd;
    border-radius: 7px;
    background: linear-gradient(var(--field-top), var(--field-bottom));
    padding: 0 20px;
    font-family: "Arimo", Arial, sans-serif;
    font-style: italic;
    font-size: 32px;
    color: var(--ink);
  }
  .email-field::placeholder { color: var(--placeholder); }
  .signup-button {
    position: absolute;
    left: 974px; top: 722px;
    width: 178px; height: 65px;
    border: 1px solid #0a2370;
    border-radius: 6px;
    background: linear-gradient(var(--button-top), var(--button-bottom));
    color: #fff;
    font-family: "Arimo", Arial, sans-serif;
    font-weight: 700;
    font-size: 31px;
    text-shadow: 0 1px 2px rgba(0,0,0,0.6);
    cursor: pointer;
  }
  .city-art { position: absolute; left: 0; top: 0; }
  .orbit-text {
    font-family: "Arimo", Arial, sans-serif;
    font-weight: 700;
    font-size: 29px;
    fill: var(--ink);
    letter-spacing: 1.5px;
  }
  .tweet-prompt {
    position: absolute;
    left: 876px; top: 976px;
    width: 230px; height: 150px;
    text-decoration: none;
  }
  .tweet-mark {
    position: absolute;
    left: 0; top: 80px;
    display: flex; align-items: center; gap: 12px;
    font-weight: 700;
    font-size: 34px;
    color: var(--chirp-text);
  }
  .tweet-mark .dot {
    width: 46px; height: 46px;
    border-radius: 50%;
    background: var(--chirp-dot);
  }
  .follow-note {
    position: absolute;
    left: 647px; top: 1124px;
    font-family: "Handlee", cursive;
    font-size: 33px;
    line-height: 40px;
    color: var(--ink);
  }
  .follow-arrow { position: absolute; left: 845px; top: 1140px; }
</style>
</head>
<body>
  <div class="night-disc"></div>

  <h1 class="brand">VentureRoster</h1>

  <p class="pitch">
    Lorem ipsum dolor sit amet,<br>
    consectetuer adipiscing elit, sed<br>
    diam nonummy nibh euismod<br>
    tincidunt ut laoreet dolore magna<br>
    aliquam erat volutpat. Ut wisi enim<br>
    ad minim veniam, quis nostrud<br>
    exerci tation ullamcorper suscipit<br>
    lobortis nisl ut aliquip ex ea<br>
    commodo consequat. Duis autem
  </p>

  <form class="signup-form" action="#">
    <input class="email-field" type="email" name="email" placeholder="Enter your Email" aria-label="Email">
    <button class="signup-button" type="submit">SIGN UP</button>
  </form>

  <svg class="city-art" width="600" height="1100" viewBox="0 0 600 1100">
    <defs>
      <linearGradient id="globe-fill" x1="0" y1="0" x2="0" y2="1">
        <stop offset="0" stop-color="var(--globe-top)"/>
        <stop offset="1" stop-color="var(--globe-bottom)"/>
      </linearGradient>
      <linearGradient id="skyline-fill" x1="0" y1="0" x2="0" y2="1">
        <stop offset="0" stop-color="var(--skyline-top)"/>
        <stop offset="1" stop-color="var(--skyline-bottom)"/>
      </linearGradient>
      <path id="orbit" d="M347 705 A154 154 0 1 1 347 1013 A154 154 0 1 1 347 705"/>
    </defs>
    <rect class="skyline-area" role="img" aria-label="Silhouette of city skyscrapers rising from the globe"
      x="150" y="420" width="240" height="420" rx="12"
      fill="url(#skyline-fill)" transform="rotate(-24 270 630)"/>
    <circle cx="347" cy="859" r="144" fill="var(--sky)"/>
    <circle cx="347" cy="859" r="139" fill="url(#globe-fill)"/>
    <text class="orbit-text"><textPath href="#orbit" startOffset="112">Sign up</textPath></text>
    <text class="orbit-text"><textPath href="#orbit" startOffset="280">Get Listed</textPath></text>
    <text class="orbit-text"><textPath href="#orbit" startOffset="500">You're Hired</textPath></text>
  </svg>

  <a class="tweet-prompt" href="#" aria-label="Follow us on Chirpline">
    <span class="tweet-mark"><span class="dot"></span>Chirpline</span>
  </a>

  <p class="follow-note">Follow us On</p>
  <svg class="follow-arrow" width="100" height="50" viewBox="0 0 100 50" aria-hidden="true">
    <path d="M8 36 C30 40 52 34 80 12" fill="none" stroke="var(--ink)" stroke-width="1.6"/>
    <path d="M70 12 L82 10 L82 22" fill="none" stroke="var(--ink)" stroke-width="1.6"/>
  </svg>
</body>
</html>
```